Building Referrer Relationships Booklet

4 page A4 booklet to give to potential professional referrers to establish a collaborative relationship.Needs to be bright, vibrant, colourful, friendly, inviting, in keeping with The Stride Studio colours.
Want to provide potential referrer partners a great reason to choose to collaborate with us. They need to know who we are, what makes us different/appealing, and who we are looking for to connect with.
The final product should communicate high performance and connectedness.

Target Market(s)

professional medical allied health and fitness practitioners

Industry/Entity Type

Health

Requirements
Must have
• energetic, vibrant, engaging, inviting, images

```html
<!DOCTYPE html>
<html lang="en">
<head>
<meta charset="utf-8">
<title>Referral Partnerships – The Stride Studio</title>
<link rel="stylesheet" href="https://fonts.googleapis.com/css2?family=Montserrat:ital,wght@0,600;1,300&family=Oswald:wght@400&display=swap">
<style>
  :root {
    --orange: #f7890f;
    --paper: #fafafa;
    --ink: #111111;
    --white: #ffffff;
    --photo-warm: #d9a46e;
    --photo-deep: #7a4a2a;
  }
  html, body {
    margin: 0;
    padding: 0;
    overflow: hidden;
    background: var(--paper);
  }
  .page {
    position: relative;
    width: 848px;
    height: 1200px;
    background: var(--paper);
    overflow: hidden;
  }
  .wave {
    position: absolute;
    left: 0;
    width: 848px;
  }
  .wave--top { top: 0; }
  .wave--bottom { bottom: 0; }
  .title-banner {
    position: absolute;
    left: 135px;
    top: 145px;
    width: 578px;
    height: 77px;
    background: var(--orange);
    display: flex;
    align-items: center;
    justify-content: center;
  }
  .title {
    margin: 0;
    font-family: "Montserrat", sans-serif;
    font-weight: 600;
    font-size: 47px;
    color: var(--white);
    letter-spacing: 1px;
  }
  .tagline {
    position: absolute;
    top: 280px;
    left: 0;
    width: 100%;
    margin: 0;
    text-align: center;
    font-family: "Montserrat", sans-serif;
    font-style: italic;
    font-weight: 300;
    font-size: 35px;
    color: var(--ink);
  }
  .statement {
    position: absolute;
    left: 110px;
    width: 628px;
    margin: 0;
    text-align: center;
    font-family: "Oswald", sans-serif;
    font-weight: 400;
    font-size: 25px;
    line-height: 32px;
    color: var(--orange);
  }
  .statement--mission { top: 418px; }
  .statement--invite { top: 920px; }
  .team-photo {
    position: absolute;
    left: 194px;
    top: 527px;
    width: 486px;
    height: 322px;
    background: radial-gradient(circle at 45% 45%, var(--photo-warm) 0%, #c98a55 55%, var(--photo-deep) 100%);
  }
</style>
</head>
<body>
  <main class="page">
    <svg class="wave wave--top" viewBox="0 0 848 125" height="125" aria-hidden="true">
      <path d="M0 0 H848 V0 C600 20 300 60 0 121 Z" fill="var(--orange)"/>
    </svg>

    <div class="title-banner">
      <h1 class="title">Referral Partnerships</h1>
    </div>

    <p class="tagline">Because Together We Achieve More</p>

    <p class="statement statement--mission">We are here to help our clients get back on their feet.</p>

    <div class="team-photo" role="img" aria-label="Photo of a team stacking their hands together in a circle over a wooden floor"></div>

    <p class="statement statement--invite">Let’s combine our skillsets so we can achieve even better results.</p>

    <svg class="wave wave--bottom" viewBox="0 0 848 125" height="125" aria-hidden="true">
      <path d="M0 125 H848 V4 C600 50 300 100 0 125 Z" fill="var(--orange)"/>
    </svg>
  </main>
</body>
</html>
```